Corvane 718Q

We are a consulting firm we a bad website and would like it to look more professional. We are a consulting firm that help people with the 340b drug program. We help non profit clinics get more funding.

Please reference our current website https://www.corvane718q.com/ for ideas

We also want a seperate webpage for each of "our services" see attachments.

Industry/Entity Type

consulting, medical, compliance

Coding

Coded - Design and coding required

Number of Pages Required

5+ page

Requirements
Must have
• Professional, my logo from my original website. It should look good
Nice to have
• It needs to be professional

```html
<!DOCTYPE html>
<html lang="en">
<head>
<meta charset="utf-8">
<title>Corvane 718Q — Why Corvane718Q</title>
<link href="https://fonts.googleapis.com/css2?family=Plus+Jakarta+Sans:wght@400;500;600;700;800&display=swap" rel="stylesheet">
<style>
:root{
  --navy:#0c2747;
  --navy-deep:#081d36;
  --teal:#14917a;
  --teal-light:#2bb596;
  --mint:#e8f5f1;
  --page:#f5f8f8;
  --ink:#13263d;
  --muted:#5c6b7c;
  --line:#dbe5e3;
  --white:#ffffff;
}
*{box-sizing:border-box;margin:0;padding:0}
html,body{width:798px;height:1200px;overflow:hidden}
body{font-family:"Plus Jakarta Sans",Arial,sans-serif;color:var(--ink);background:var(--white);font-size:6px;line-height:1.45}
.wrap{padding:0 26px}

/* header */
.site-header{height:32px;display:flex;align-items:center;justify-content:space-between;padding:0 26px;background:var(--white);border-bottom:1px solid var(--line)}
.brand{display:flex;align-items:center;gap:6px;font-weight:700;font-size:13px;color:var(--navy)}
.brand-dot{width:16px;height:16px;border-radius:50%;background:var(--teal)}
.nav{display:flex;gap:20px;font-size:6.5px;font-weight:600;color:var(--ink)}
.nav .active{color:var(--teal);border-bottom:1.5px solid var(--teal);padding-bottom:2px}
.btn{display:inline-flex;align-items:center;gap:4px;font-weight:700;font-size:6.2px;padding:7px 11px;border-radius:3px}
.btn-navy{background:var(--navy);color:var(--white)}
.btn-teal{background:var(--teal);color:var(--white)}
.btn-ghost{border:1px solid var(--navy);color:var(--navy);background:var(--white)}
.btn-outline-light{border:1px solid rgba(255,255,255,.6);color:var(--white)}

/* hero */
.hero{height:222px;display:flex;background:linear-gradient(90deg,var(--page) 0 50%,#dfe9ec 50%)}
.hero-copy{width:50%;padding:18px 26px 0}
.crumb{font-size:5.5px;color:var(--muted);margin-bottom:14px}
.eyebrow{font-size:5.5px;font-weight:700;letter-spacing:.8px;color:var(--teal);text-transform:uppercase}
.hero h1{font-size:25px;line-height:1.1;font-weight:800;color:var(--navy);margin:6px 0 10px}
.hero h1 span{color:var(--teal)}
.hero p{font-size:6.5px;color:var(--muted);max-width:300px;margin-bottom:14px}
.hero .actions{display:flex;gap:8px}
.hero-photo{width:50%;background:linear-gradient(135deg,#c9d8df,#8fa7b6 60%,#6d889b)}

/* section headings */
.sec-head{text-align:center;margin-bottom:12px}
.sec-head h2{font-size:14px;font-weight:800;color:var(--navy);margin-top:3px}

/* reasons */
.reasons{padding:14px 26px 16px;background:var(--white)}
.reason-grid{display:grid;grid-template-columns:repeat(6,1fr);gap:7px}
.reason{border:1px solid var(--line);border-radius:5px;padding:10px 7px;text-align:center;background:var(--white)}
.reason .icon{width:22px;height:22px;margin:0 auto 6px;border-radius:50%;background:var(--mint);display:flex;align-items:center;justify-content:center}
.reason h3{font-size:6.6px;font-weight:700;color:var(--navy);margin-bottom:4px}
.reason p{font-size:5px;color:var(--muted)}

/* results */
.results{background:var(--navy);color:var(--white);padding:16px 26px 18px;height:160px}
.results .eyebrow{color:var(--teal-light)}
.results h2{font-size:15px;font-weight:800;margin:4px 0 14px}
.stats{display:grid;grid-template-columns:repeat(5,1fr);gap:8px}
.stat{border:1px solid rgba(255,255,255,.18);border-radius:5px;padding:12px 10px;display:flex;gap:6px;align-items:flex-start}
.stat strong{font-size:17px;font-weight:800;line-height:1}
.stat small{font-size:5px;opacity:.8;display:block;margin-top:3px}

/* mission */
.mission{display:flex;gap:24px;padding:20px 26px;background:var(--page);height:210px}
.mission-photo{width:48%;border-radius:6px;background:linear-gradient(160deg,#b9cde0,#7f99a9 55%,#5e7765)}
.mission-copy{flex:1;padding-top:4px}
.mission h2{font-size:15px;font-weight:800;color:var(--navy);margin:4px 0 6px}
.mission h2 span{color:var(--teal)}
.mission p.lead{font-size:6px;color:var(--muted);margin-bottom:12px}
.ticks{display:grid;grid-template-columns:1fr 1fr;gap:10px 14px;margin-bottom:12px}
.tick{display:flex;gap:5px}
.tick b{font-size:6.3px;color:var(--navy);display:block}
.tick span{font-size:5px;color:var(--muted)}

/* testimonials */
.testimonials{padding:16px 26px;height:190px;background:var(--white)}
.quotes{display:grid;grid-template-columns:repeat(3,1fr);gap:10px}
.quote{border:1px solid var(--line);border-radius:5px;padding:12px}
.quote .mark{color:var(--teal);font-size:16px;font-weight:800;line-height:.8}
.quote p{font-size:5.6px;color:var(--muted);margin:4px 0 10px}
.who{display:flex;gap:6px;align-items:center}
.avatar{width:18px;height:18px;border-radius:50%;background:#c7d6d3}
.who b{font-size:6px;color:var(--navy);display:block}
.who span{font-size:5px;color:var(--muted)}
.stars{margin-left:auto;color:var(--teal);font-size:6px;letter-spacing:1px}

/* cta */
.cta{margin:0 26px;background:var(--navy);border-radius:6px;padding:12px 16px;display:flex;align-items:center;justify-content:space-between;color:var(--white);height:44px}
.cta h3{font-size:10px;font-weight:800}
.cta p{font-size:5.5px;opacity:.8}
.cta .actions{display:flex;gap:8px}

/* footer */
.site-footer{background:var(--navy-deep);color:#c8d3df;margin-top:-22px;padding:36px 26px 0;height:172px}
.foot-grid{display:grid;grid-template-columns:1.6fr 1fr 1.3fr 1fr 1.2fr;gap:16px}
.site-footer .brand{color:var(--white);margin-bottom:6px}
.site-footer h4{font-size:6.3px;color:var(--white);margin-bottom:6px}
.site-footer li{list-style:none;font-size:5.4px;margin-bottom:4px}
.site-footer p{font-size:5.4px}
.social{display:flex;gap:5px;margin-top:8px}
.social i{width:11px;height:11px;border-radius:50%;background:rgba(255,255,255,.18)}
.foot-bottom{border-top:1px solid rgba(255,255,255,.12);margin-top:14px;padding-top:8px;font-size:5px;display:flex;justify-content:space-between}
</style>
</head>
<body>

<header class="site-header">
  <div class="brand"><span class="brand-dot"></span>Corvane718Q</div>
  <nav class="nav">
    <span>Home</span><span>About Us</span><span>Our Services ▾</span><span class="active">Why Corvane718Q</span><span>Resources ▾</span><span>Contact Us</span>
  </nav>
  <a class="btn btn-navy">Schedule a Consultation →</a>
</header>

<section class="hero">
  <div class="hero-copy">
    <div class="crumb">Home › Why Corvane718Q</div>
    <div class="eyebrow">Why Corvane718Q</div>
    <h1>More Than Expertise.<br><span>A True Partner.</span></h1>
    <p>We combine specialized 340B knowledge, proven processes, and a passion for community health to help you achieve sustainable results that make a difference.</p>
    <div class="actions">
      <a class="btn btn-teal">Schedule a Consultation →</a>
      <a class="btn btn-ghost">Explore Our Services →</a>
    </div>
  </div>
  <div class="hero-photo" role="img" aria-label="Photo of consultants meeting with clinic staff around a table"></div>
</section>

<section class="reasons">
  <div class="sec-head">
    <div class="eyebrow">The Corvane718Q Difference</div>
    <h2>Why Covered Entities Choose Us</h2>
  </div>
  <div class="reason-grid">
    <div class="reason"><div class="icon"><svg width="11" height="11" viewBox="0 0 12 12"><circle cx="6" cy="6" r="4.5" fill="none" stroke="#14917a" stroke-width="1.3"/></svg></div><h3>Deep 340B Expertise</h3><p>Our team lives and breathes 340B with years of regulatory and audit know-how.</p></div>
    <div class="reason"><div class="icon"><svg width="11" height="11" viewBox="0 0 12 12"><path d="M6 10.5 1.5 6A2.4 2.4 0 0 1 6 3a2.4 2.4 0 0 1 4.5 3z" fill="#14917a"/></svg></div><h3>Healthcare Focused</h3><p>We understand the unique challenges of health centers and clinics we serve.</p></div>
    <div class="reason"><div class="icon"><svg width="11" height="11" viewBox="0 0 12 12"><path d="M2 6.3 5 9l5-6" fill="none" stroke="#14917a" stroke-width="1.5"/></svg></div><h3>Compliance You Can Trust</h3><p>Proven processes and audit-ready documentation keep your program protected.</p></div>
    <div class="reason"><div class="icon"><svg width="11" height="11" viewBox="0 0 12 12"><path d="M2 10V7m4 3V4m4 6V2" stroke="#14917a" stroke-width="1.6"/></svg></div><h3>Measurable Impact</h3><p>We focus on what matters most: savings, access, and real healthier communities.</p></div>
    <div class="reason"><div class="icon"><svg width="11" height="11" viewBox="0 0 12 12"><circle cx="4" cy="5" r="2" fill="#14917a"/><circle cx="8.5" cy="5" r="2" fill="#14917a"/></svg></div><h3>True Partnership</h3><p>We work alongside you as an extension of your team, invested in your success.</p></div>
    <div class="reason"><div class="icon"><svg width="11" height="11" viewBox="0 0 12 12"><path d="M6 1.5 10 3v3.3C10 8.6 8.2 10 6 10.8 3.8 10 2 8.6 2 6.3V3z" fill="#14917a"/></svg></div><h3>Mission Driven</h3><p>We share your mission to improve care and strengthen the communities you serve.</p></div>
  </div>
</section>

<section class="results">
  <div class="eyebrow">Proven. Trusted. Impactful.</div>
  <h2>Results That Speak for Themselves</h2>
  <div class="stats">
    <div class="stat"><div><strong>300+</strong><small>Covered Entity Audits Supported</small></div></div>
    <div class="stat"><div><strong>$2B+</strong><small>In Estimated Savings Recovered for Clients</small></div></div>
    <div class="stat"><div><strong>99%+</strong><small>Client Satisfaction Rate Year Over Year</small></div></div>
    <div class="stat"><div><strong>18+</strong><small>Years of Combined 340B Experience</small></div></div>
    <div class="stat"><div><strong>Stronger</strong><small>Communities Through Better Care</small></div></div>
  </div>
</section>

<section class="mission">
  <div class="mission-photo" role="img" aria-label="Photo of a community health center building exterior"></div>
  <div class="mission-copy">
    <div class="eyebrow">Our Commitment</div>
    <h2>Your Mission. <span>Our Commitment.</span></h2>
    <p class="lead">We are committed to helping covered entities expand access to care, strengthen their 340B programs, and create healthier communities.</p>
    <div class="ticks">
      <div class="tick"><svg width="9" height="9" viewBox="0 0 10 10"><circle cx="5" cy="5" r="5" fill="#14917a"/><path d="M2.8 5.2 4.4 6.7 7.3 3.6" fill="none" stroke="#fff" stroke-width="1.2"/></svg><div><b>We listen first.</b><span>Understanding your goals and challenges.</span></div></div>
      <div class="tick"><svg width="9" height="9" viewBox="0 0 10 10"><circle cx="5" cy="5" r="5" fill="#14917a"/><path d="M2.8 5.2 4.4 6.7 7.3 3.6" fill="none" stroke="#fff" stroke-width="1.2"/></svg><div><b>We deliver results.</b><span>Focused on measurable impact and compliance.</span></div></div>
      <div class="tick"><svg width="9" height="9" viewBox="0 0 10 10"><circle cx="5" cy="5" r="5" fill="#14917a"/><path d="M2.8 5.2 4.4 6.7 7.3 3.6" fill="none" stroke="#fff" stroke-width="1.2"/></svg><div><b>We act with integrity.</b><span>Transparent, honest, and mission-focused.</span></div></div>
      <div class="tick"><svg width="9" height="9" viewBox="0 0 10 10"><circle cx="5" cy="5" r="5" fill="#14917a"/><path d="M2.8 5.2 4.4 6.7 7.3 3.6" fill="none" stroke="#fff" stroke-width="1.2"/></svg><div><b>We care deeply.</b><span>About your mission, your patients, and your success.</span></div></div>
    </div>
    <a class="btn btn-teal">Learn More About Us →</a>
  </div>
</section>

<section class="testimonials">
  <div class="sec-head">
    <div class="eyebrow">What Our Partners Say</div>
    <h2>Trusted by Leaders in Healthcare</h2>
  </div>
  <div class="quotes">
    <div class="quote"><div class="mark">“</div><p>Corvane718Q transformed our program. Their expertise and support helped us maximize savings and expand services to our community.</p><div class="who"><span class="avatar"></span><div><b>Dr. Mirela Okonde</b><span>CEO, Community Health Center</span></div><span class="stars">★★★★★</span></div></div>
    <div class="quote"><div class="mark">“</div><p>Their team is responsive, knowledgeable, and truly invested in our success. We couldn't ask for a better partner.</p><div class="who"><span class="avatar"></span><div><b>Tobias N. Harlow</b><span>Chief Financial Officer</span></div><span class="stars">★★★★★</span></div></div>
    <div class="quote"><div class="mark">“</div><p>Thanks to Corvane718Q, we are more compliant, more efficient, and able to do more for the patients we serve every day.</p><div class="who"><span class="avatar"></span><div><b>Priya D. Castellan</b><span>Director of Pharmacy Services</span></div><span class="stars">★★★★★</span></div></div>
  </div>
</section>

<section class="cta">
  <div>
    <h3>Let's Build a Stronger 340B Program—Together</h3>
    <p>Schedule a consultation to learn how we can help your organization thrive.</p>
  </div>
  <div class="actions">
    <a class="btn btn-navy" style="background:#fff;color:#0c2747">Schedule a Consultation →</a>
    <a class="btn btn-outline-light">Explore Our Services →</a>
  </div>
</section>

<footer class="site-footer">
  <div class="foot-grid">
    <div>
      <div class="brand"><span class="brand-dot"></span>Corvane718Q</div>
      <p>Helping covered entities strengthen 340B programs, stay compliant, and expand access to care for the communities they serve.</p>
      <div class="social"><i></i><i></i><i></i></div>
    </div>
    <div><h4>Quick Links</h4><ul><li>Home</li><li>About Us</li><li>Why Corvane718Q</li><li>Resources</li><li>Contact Us</li></ul></div>
    <div><h4>Our Services</h4><ul><li>340B Program Management</li><li>Compliance &amp; Audit Support</li><li>Contract Pharmacy Oversight</li><li>Policy &amp; Procedure Development</li><li>Training &amp; Education</li></ul></div>
    <div><h4>Resources</h4><ul><li>Blog</li><li>Guides &amp; Toolkits</li><li>Webinars</li><li>FAQs</li></ul></div>
    <div><h4>Contact Us</h4><ul><li>(555) 014-7180</li><li>hello@corvane718q.com</li><li>www.corvane718q.com</li></ul></div>
  </div>
  <div class="foot-bottom"><span>© 2025 Corvane718Q. All rights reserved.</span><span>Privacy Policy · Terms of Use</span></div>
</footer>

</body>
</html>
```